Veltrano Energy Business Card Design

website: www.veltranoenergy.example
Project: Business Card Design for Veltrano Energy
Name: Dorian Kettle
Title: Founder / Operations Strategist
Visual Identity & Logo:
Logo File: VEL-Logo-FullGradient-Final.png (Attached).
Color Palette: The brand relies on a distinctive Cyan (Blue) to Lime Green gradient.
Background Preference: We want a Dark Mode aesthetic (Deep Matte Black, Charcoal, or Dark Slate) to make the neon gradient of the logo pop. This feels more "tech/industrial" than a standard white card.
Design Aesthetic (The "Ops" Vibe):
Concept: "Grid & Infrastructure." We are a solar rental company, focusing on logistics and access.
Typography: White, bold sans-serif text for contact info. High contrast against the dark background.
Accents: Use the Cyan or Lime Green from the logo for thin divider lines or edge painting.
Avoid: No orange/gold (clashes with logo). No cartoon leaves.
Layout Requirements:
Front: Large, centered logo. Maybe a subtle UV gloss spot varnish over the logo icon.
Back: Name, Title, Contact Info.
Texture: Matte finish cardstock with gloss elements.
sample mock up of information on card: https://brivomarkco-my.filehost.example/:i:/g/personal/dorian_kettle_veltranoenergy_example/AbCdEfGhIjKlMnOpQrStUvWxYz012345678?e=Xy12Ab
Logo: https://brivomarkco.filehost.example/:i:/s/VeltranoEnergy/ZyXwVuTsRqPoNmLkJiHgFeDcBa9876543210?e=Pq34Cd

```html
<!DOCTYPE html>
<html lang="en">
<head>
<meta charset="utf-8">
<title>Veltrano Energy Business Card</title>
<link rel="stylesheet" href="https://fonts.googleapis.com/css2?family=Montserrat:wght@400;500;700;800&family=Open+Sans:ital,wght@1,600&display=swap">
<style>
  :root {
    --backdrop: #3b3b3c;
    --card: #262627;
    --emboss: #3a3a3b;
    --emboss-mark: #1c1c1d;
    --cyan: #16a6dc;
    --lime: #b6d334;
    --white: #f4f4f4;
  }
  * { box-sizing: border-box; margin: 0; padding: 0; }
  html, body {
    width: 1200px; height: 875px; overflow: hidden;
    background: var(--backdrop);
    font-family: "Montserrat", Arial, sans-serif;
  }
  .sheet {
    width: 1200px; height: 875px;
    display: flex; flex-direction: column; align-items: center; justify-content: center;
    gap: 48px;
  }
  .card {
    position: relative;
    width: 620px; height: 354px;
    background: var(--card);
    box-shadow: 0 14px 30px rgba(0,0,0,.45);
    overflow: hidden;
    white-space: nowrap;
  }
  .card::before {
    content: ""; position: absolute; left: 0; top: 0; bottom: 0; width: 3px;
    background: linear-gradient(to bottom, var(--cyan), #5fbf9a);
  }
  .card::after {
    content: ""; position: absolute; left: 0; right: 0; bottom: 0; height: 3px;
    background: linear-gradient(to right, #5fbf9a, var(--lime));
  }

  /* Front */
  .front-mark {
    position: absolute; left: 90px; top: 88px;
    display: flex; align-items: center; gap: 22px;
  }
  .front-mark .mark-square {
    width: 64px; height: 64px; background: var(--emboss-mark);
  }
  .front-mark .wordmark {
    font-weight: 500; font-size: 44px; letter-spacing: .5px;
    color: var(--emboss); line-height: 1;
  }
  .front .tagline {
    position: absolute; left: 200px; top: 186px;
    font-family: "Open Sans", Arial, sans-serif; font-style: italic; font-weight: 600;
    font-size: 17px; color: var(--white); letter-spacing: .3px;
  }
  .front .promise {
    position: absolute; left: 70px; bottom: 36px;
    font-size: 17px; font-weight: 500; letter-spacing: .6px;
    background: linear-gradient(to right, var(--cyan), var(--lime));
    -webkit-background-clip: text; background-clip: text; color: transparent;
  }

  /* Back */
  .back-mark {
    position: absolute; left: 200px; top: 54px;
    display: flex; align-items: center; gap: 14px;
  }
  .back-mark .mark-square { width: 44px; height: 44px; background: var(--cyan); }
  .back-mark .wordmark {
    font-weight: 500; font-size: 34px; color: var(--cyan); line-height: 1;
  }
  .identity { position: absolute; left: 48px; top: 158px; }
  .identity .person {
    font-weight: 800; font-size: 24px; letter-spacing: .5px; text-transform: uppercase;
    background: linear-gradient(to right, var(--cyan), var(--lime));
    -webkit-background-clip: text; background-clip: text; color: transparent;
  }
  .identity .role {
    margin-top: 4px; font-size: 14px; font-weight: 500; color: var(--white);
  }
  .divider {
    position: absolute; left: 328px; top: 140px; width: 1px; height: 96px;
    background: linear-gradient(to bottom, var(--cyan), var(--lime));
  }
  .contacts {
    position: absolute; left: 346px; top: 142px;
    list-style: none; display: flex; flex-direction: column; gap: 10px;
  }
  .contacts li {
    display: flex; align-items: center; gap: 9px;
    font-size: 13.5px; font-weight: 500; color: var(--white);
  }
  .contacts svg { width: 14px; height: 14px; flex: none; }
  .address {
    position: absolute; left: 48px; bottom: 40px;
    font-size: 14px; font-weight: 500; color: var(--white); letter-spacing: .3px;
  }
</style>
</head>
<body>
<main class="sheet">

  <section class="card front" aria-label="Card front">
    <div class="front-mark">
      <span class="mark-square"></span>
      <span class="wordmark">Veltrano Energy</span>
    </div>
    <p class="tagline">Rent Solar. Generate Power. Save Smarter</p>
    <p class="promise">No debt, no liens, no maintenance, just savings.</p>
  </section>

  <section class="card back" aria-label="Card back">
    <div class="back-mark">
      <span class="mark-square"></span>
      <span class="wordmark">Veltrano Energy</span>
    </div>

    <div class="identity">
      <h1 class="person">Dorian Kettle</h1>
      <p class="role">Founder / Operations Strategist</p>
    </div>

    <span class="divider"></span>

    <ul class="contacts">
      <li>
        <svg viewBox="0 0 16 16" aria-hidden="true"><path fill="#b6d334" d="M3.5 1.5l2.6 2.6-1.4 1.9c.9 1.9 2.4 3.4 4.3 4.3l1.9-1.4 2.6 2.6-1.6 2.3C6.6 13.5 2.5 9.4 1.2 3.1z"/></svg>
        555.014.2290
      </li>
      <li>
        <svg viewBox="0 0 16 16" aria-hidden="true"><rect x="1" y="3" width="14" height="10" fill="#b6d334"/><path d="M1 3l7 6 7-6" fill="none" stroke="#262627" stroke-width="1.4"/></svg>
        info@veltranoenergy.example
      </li>
      <li>
        <svg viewBox="0 0 16 16" aria-hidden="true"><g fill="none" stroke="#b6d334" stroke-width="1.4"><circle cx="8" cy="8" r="6.5"/><ellipse cx="8" cy="8" rx="2.8" ry="6.5"/><path d="M1.5 8h13"/></g></svg>
        www.veltranoenergy.example
      </li>
    </ul>

    <p class="address">Veltrano Energy, LLC 4120 Harrow Creek Lane Marlow, FL 30000</p>
  </section>

</main>
</body>
</html>
```